Retail Jewelry Business Card Design Project

We are in need of a new business card design for a retail jewelry store. This store is in the business of fine jewelry including but not specific to bridal jewelry, diamonds, designer jewelry and watches.

This store has been in business for 20 years but continues to strive for a modern professional appeal. The main colors use for this business are a royal blue, white and silver.

Target Market(s)

Target market is ages 18-50

Industry/Entity Type

Jewelry

Requirements
Must have
• Sales Person Name
Sales Person Email Address

Store Address
Store Phone
Website

Standard business card size. No odd shapes or sizes.
Nice to have
• Overall modern feel for card.

We have thought that a design with a nice feature of the logo on the back of the card would be nice but open to ideas.
Should not have
• No specific images of jewelry should be used.

```html
<!DOCTYPE html>
<html lang="en">
<head>
<meta charset="utf-8">
<title>Marcus Hale Fine Jewelry – Business Cards</title>
<link rel="stylesheet" href="https://fonts.googleapis.com/css2?family=Lora:wght@400;600&display=swap">
<style>
  :root {
    --royal-blue: #2b2fa6;
    --royal-blue-deep: #1c1f86;
    --royal-blue-light: #3d44c4;
    --pearl: #f7f6f2;
    --pearl-shade: #dcdad4;
    --silver: #c9ccd6;
    --white: #ffffff;
    --page: #ececec;
  }
  * { box-sizing: border-box; margin: 0; padding: 0; }
  html, body { width: 1200px; height: 1024px; overflow: hidden; }
  body {
    background: var(--page);
    font-family: "Lora", Georgia, serif;
    position: relative;
  }
  .card {
    position: absolute;
    width: 700px;
    height: 400px;
    overflow: hidden;
    box-shadow: 0 6px 18px rgba(0,0,0,0.18);
  }
  .card__fabric {
    position: absolute; inset: 0;
  }
  .card--front { left: 100px; top: 70px; }
  .card--front .card__fabric {
    background: linear-gradient(135deg, var(--white) 0%, var(--pearl-shade) 30%, var(--pearl) 55%, var(--pearl-shade) 78%, var(--white) 100%);
  }
  .card--back { left: 400px; top: 550px; }
  .card--back .card__fabric {
    background: linear-gradient(150deg, var(--royal-blue-light) 0%, var(--royal-blue-deep) 35%, var(--royal-blue) 60%, var(--royal-blue-deep) 100%);
  }
  .brand {
    position: absolute;
    text-align: center;
    font-weight: 600;
    line-height: 1.1;
  }
  .brand__name { font-size: 58px; display: block; }
  .brand__tag { font-size: 24px; letter-spacing: 6px; display: block; margin-top: 6px; }
  .card--front .brand { left: 40px; top: 70px; width: 380px; color: var(--royal-blue); }
  .card--back .brand { left: 0; right: 0; top: 120px; color: var(--white); }
  .person {
    position: absolute; left: 40px; top: 220px; width: 380px;
    text-align: center; color: var(--royal-blue); font-size: 22px;
  }
  .contact {
    position: absolute; left: 40px; bottom: 40px;
    list-style: none; color: var(--royal-blue); font-size: 19px;
  }
  .contact li { display: flex; align-items: center; gap: 10px; margin-top: 8px; }
  .contact svg { width: 18px; height: 18px; fill: var(--royal-blue); flex: none; }
  .website {
    position: absolute; left: 40px; bottom: 36px;
    color: var(--white); font-size: 18px;
  }
</style>
</head>
<body>
  <section class="card card--front" aria-label="Business card front">
    <div class="card__fabric" role="img" aria-label="White satin fabric background"></div>
    <div class="brand">
      <span class="brand__name">Marcus Hale</span>
      <span class="brand__tag">FINE JEWELRY</span>
    </div>
    <p class="person">Marcus Hale Brennan</p>
    <ul class="contact">
      <li>
        <svg viewBox="0 0 20 20" aria-hidden="true"><path d="M10 2 1 10h3v8h5v-5h2v5h5v-8h3z"/></svg>
        2280 Linden Avenue Bayport, FL 32000
      </li>
      <li>
        <svg viewBox="0 0 20 20" aria-hidden="true"><path d="M5 1h10a1 1 0 0 1 1 1v16a1 1 0 0 1-1 1H5a1 1 0 0 1-1-1V2a1 1 0 0 1 1-1zm1 2v12h8V3z"/></svg>
        000-000-000
        <svg viewBox="0 0 20 20" aria-hidden="true"><path d="M1 4h18v12H1zm2 2v.5l7 5 7-5V6l-7 5z"/></svg>
        marcus@marcushalejewelry.com
      </li>
      <li>
        <svg viewBox="0 0 20 20" aria-hidden="true"><path d="M10 1a9 9 0 1 0 0 18 9 9 0 0 0 0-18zm0 2c1.2 1.5 2 4 2 7s-.8 5.5-2 7c-1.2-1.5-2-4-2-7s.8-5.5 2-7zM3.2 9h3.8c0-1.5.3-3 .8-4.2A7 7 0 0 0 3.2 9zm9.8 0h3.8a7 7 0 0 0-4.6-4.2c.5 1.2.8 2.7.8 4.2zM3.2 11a7 7 0 0 0 4.6 4.2c-.5-1.2-.8-2.7-.8-4.2zm9.8 0c0 1.5-.3 3-.8 4.2a7 7 0 0 0 4.6-4.2z"/></svg>
        www.marcushalejewelry.com
      </li>
    </ul>
  </section>

  <section class="card card--back" aria-label="Business card back">
    <div class="card__fabric" role="img" aria-label="Royal blue satin fabric background"></div>
    <div class="brand">
      <span class="brand__name">Marcus Hale</span>
      <span class="brand__tag">FINE JEWELRY</span>
    </div>
    <p class="website">www.marcushalejewelry.com</p>
  </section>
</body>
</html>
```